Need a business card for our overland brand!

We had the logo made and we need a great design for our business card. Use the logo provide or tweak it however you see fit.

Contact Information for Business Card

Name, Title, Telephone, email, website

```html
<!DOCTYPE html>
<html lang="en">
<head>
<meta charset="utf-8">
<title>Ridgeway Transit — Business Card</title>
<link rel="stylesheet" href="https://fonts.googleapis.com/css2?family=Oswald:wght@600&family=Montserrat:wght@400;500&display=swap">
<style>
  :root {
    --navy: #213753;
    --navy-deep: #1b2e47;
    --teal: #1fa3c8;
    --sky: #6f9fd8;
    --white: #ffffff;
    --backdrop: #3a3431;
  }
  * { margin: 0; padding: 0; box-sizing: border-box; }
  html, body { width: 1200px; height: 716px; overflow: hidden; }
  body {
    background: var(--backdrop);
    position: relative;
    font-family: "Montserrat", sans-serif;
  }
  .card {
    position: absolute;
    top: 210px;
    width: 520px;
    height: 297px;
    border-radius: 6px;
    overflow: hidden;
    box-shadow: 0 10px 28px rgba(0,0,0,0.45);
  }
  .card-front { left: 60px; background: var(--navy); }
  .card-back { left: 620px; background: var(--white); }

  .front-scenery {
    position: absolute;
    left: 0; top: 120px;
    width: 330px; height: 177px;
    background: linear-gradient(160deg, rgba(27,46,71,0) 0%, rgba(27,46,71,0.9) 45%, rgba(111,159,216,0.55) 100%);
  }
  .brand-name {
    font-family: "Oswald", sans-serif;
    font-weight: 600;
    text-transform: uppercase;
    line-height: 0.92;
    letter-spacing: 0.5px;
  }
  .front-brand {
    position: absolute;
    left: 300px; top: 88px;
    font-size: 44px;
    color: var(--white);
  }
  .back-brand {
    position: absolute;
    left: 30px; top: 26px;
    font-size: 38px;
    color: var(--navy);
  }
  .back-waves { position: absolute; left: 0; top: 0; width: 520px; height: 297px; }

  .holder {
    position: absolute;
    right: 36px; top: 76px;
    text-align: right;
  }
  .holder-name {
    font-family: "Oswald", sans-serif;
    font-weight: 600;
    font-size: 22px;
    line-height: 1.2;
    text-transform: uppercase;
    color: var(--navy);
    letter-spacing: 0.5px;
  }
  .holder-name .first { color: var(--teal); }
  .holder-title { font-size: 11px; color: var(--navy); }

  .contact {
    position: absolute;
    right: 26px; bottom: 18px;
    text-align: right;
    color: var(--white);
    font-size: 11px;
    line-height: 1.45;
  }
  .contact .address { margin-bottom: 5px; padding-right: 16px; }
  .contact-line { display: flex; justify-content: flex-end; align-items: center; gap: 6px; }
  .contact-line svg { width: 10px; height: 10px; flex: none; }
</style>
</head>
<body>

  <section class="card card-front">
    <div class="front-scenery" role="img" aria-label="Mountain ridge silhouette in soft blue tones"></div>
    <div class="brand-name front-brand">Ridgeway<br>Transit</div>
  </section>

  <section class="card card-back">
    <svg class="back-waves" viewBox="0 0 520 297" aria-hidden="true">
      <path d="M0,128 C60,180 180,174 300,168 C400,164 470,156 520,146 L520,297 L0,297 Z" fill="var(--navy)"/>
      <path d="M0,120 C60,172 180,166 300,160 C400,156 470,148 520,138" fill="none" stroke="var(--white)" stroke-width="8"/>
      <path d="M0,118 C60,168 180,162 300,156 C400,152 470,144 520,134" fill="none" stroke="var(--teal)" stroke-width="5"/>
      <path d="M0,110 C40,145 120,158 250,152" fill="none" stroke="var(--navy)" stroke-width="3"/>
    </svg>

    <div class="brand-name back-brand">Ridgeway<br>Transit</div>

    <div class="holder">
      <div class="holder-name"><span class="first">Dale</span> Whitford</div>
      <div class="holder-title">Founder</div>
    </div>

    <div class="contact">
      <div class="address">4120 North Cedar Avenue<br>#18, Suite Pine Hollow</div>
      <div class="contact-line">+1- 555-014-2290
        <svg viewBox="0 0 10 10"><path d="M2,1 L4,1 L4.5,3 L3.5,4 C4,5.3 4.8,6 6,6.5 L7,5.5 L9,6 L9,8 C5,8.5 1.5,5 2,1 Z" fill="var(--teal)"/></svg>
      </div>
      <div class="contact-line">info@ridgewaytransit.com
        <svg viewBox="0 0 10 10"><rect x="1" y="2.5" width="8" height="5.5" fill="none" stroke="var(--teal)" stroke-width="1"/><path d="M1,2.5 L5,5.5 L9,2.5" fill="none" stroke="var(--teal)" stroke-width="1"/></svg>
      </div>
      <div class="contact-line">www.ridgewaytransit.com
        <svg viewBox="0 0 10 10"><circle cx="5" cy="5" r="4" fill="none" stroke="var(--teal)" stroke-width="1"/><ellipse cx="5" cy="5" rx="1.8" ry="4" fill="none" stroke="var(--teal)" stroke-width="0.8"/><line x1="1" y1="5" x2="9" y2="5" stroke="var(--teal)" stroke-width="0.8"/></svg>
      </div>
    </div>
  </section>

</body>
</html>
```